Walk Bright through the Seasons: 52 Weeks to a Year of Courage and Calm

This is a non-fiction, self-help book. The first edition was published a decade ago, and it needs a new design. Nothing too literal (no actual hearts on the cover) but something inspirational or perhaps something quite plain. The current cover is below for reference, but I DO NOT want something similar to that. It is outdated.

The cover must include:

1. Title: Walk Bright through the Seasons
2. Subtitle: 52 Weeks to a Year of Courage and Calm
3. Author Name: Tobin Wells

It should also have plenty of "white space" in other words the fonts shouldnt be so big that they take up the whole cover.

Dimensions: 9" x 6.25"

Target Market(s)

adults interested in personal development

Font styles to use
Serif
Script

Colors

Designer to choose colors to be used in the design.

Requirements
Must have
• Classic look and feel. The current design is too busy. I have included examples of the style I like below. I'm open to a singular graphic/photo but nothing more than that. Probably plain text is best.
• Please look at the samples I have included of best-selling books in the genre that I like. The cover should be modeled after these.

```html
<!DOCTYPE html>
<html lang="en">
<head>
<meta charset="utf-8">
<title>Walk Bright through the Seasons — Cover Spread</title>
<link rel="stylesheet" href="https://fonts.googleapis.com/css2?family=Cormorant+Garamond:wght@400;500;600&family=Pinyon+Script&display=swap">
<style>
  :root {
    --paper: #f5f0e6;
    --paper-shade: #ece5d6;
    --ink: #1f2e3d;
    --ink-soft: #4a5664;
    --gold: #a8874f;
    --gold-light: #c7ab78;
  }
  html, body {
    margin: 0;
    padding: 0;
    width: 1200px;
    height: 933px;
    overflow: hidden;
    background: var(--paper);
  }
  .cover-spread {
    position: relative;
    width: 1200px;
    height: 933px;
    overflow: hidden;
    background: linear-gradient(180deg, var(--paper) 0%, var(--paper) 70%, var(--paper-shade) 100%);
  }
  .spine-fold {
    position: absolute;
    top: 0;
    left: 578px;
    width: 44px;
    height: 100%;
    background: linear-gradient(90deg, rgba(0,0,0,0) 0%, rgba(60,45,20,0.06) 50%, rgba(0,0,0,0) 100%);
  }

  /* Back cover */
  .back-cover {
    position: absolute;
    left: 0;
    top: 0;
    width: 578px;
    height: 100%;
  }
  .back-cover-tagline {
    position: absolute;
    left: 0;
    width: 578px;
    top: 858px;
    margin: 0;
    text-align: center;
    font-family: "Cormorant Garamond", serif;
    font-weight: 500;
    font-size: 13px;
    letter-spacing: 5px;
    color: var(--gold);
    text-transform: uppercase;
    white-space: nowrap;
  }

  /* Front cover */
  .front-cover {
    position: absolute;
    left: 622px;
    top: 0;
    width: 578px;
    height: 100%;
  }
  .title-block {
    position: absolute;
    left: 0;
    top: 250px;
    width: 578px;
    display: flex;
    flex-direction: column;
    align-items: center;
    text-align: center;
  }
  .top-rule,
  .mid-rule {
    display: block;
    width: 70px;
    height: 1px;
    background: var(--gold);
  }
  .top-rule { margin-bottom: 34px; }
  .book-title {
    margin: 0;
    font-weight: 400;
    color: var(--ink);
    line-height: 1;
  }
  .book-title span { display: block; white-space: nowrap; }
  .title-serif {
    font-family: "Cormorant Garamond", serif;
    font-weight: 500;
    font-size: 58px;
    letter-spacing: 8px;
    text-transform: uppercase;
    line-height: 62px;
    padding-left: 8px;
  }
  .title-script {
    font-family: "Pinyon Script", cursive;
    font-size: 44px;
    line-height: 58px;
    color: var(--gold);
    margin: 4px 0 6px;
  }
  .mid-rule { margin: 38px 0 26px; }
  .book-subtitle {
    margin: 0;
    font-family: "Cormorant Garamond", serif;
    font-weight: 500;
    font-size: 15px;
    letter-spacing: 2.6px;
    color: var(--ink-soft);
    text-transform: uppercase;
    white-space: nowrap;
  }
  .author-name {
    position: absolute;
    left: 0;
    width: 578px;
    top: 842px;
    margin: 0;
    text-align: center;
    font-family: "Cormorant Garamond", serif;
    font-weight: 600;
    font-size: 22px;
    letter-spacing: 7px;
    color: var(--ink);
    text-transform: uppercase;
    padding-left: 7px;
    box-sizing: border-box;
  }
</style>
</head>
<body>
  <main class="cover-spread">
    <section class="back-cover">
      <p class="back-cover-tagline">Walk Bright through the Seasons</p>
    </section>

    <div class="spine-fold"></div>

    <section class="front-cover">
      <div class="title-block">
        <span class="top-rule"></span>
        <h1 class="book-title">
          <span class="title-serif">Walk Bright</span>
          <span class="title-script">through the</span>
          <span class="title-serif">Seasons</span>
        </h1>
        <span class="mid-rule"></span>
        <p class="book-subtitle">52 Weeks to a Year of Courage and Calm</p>
      </div>
      <p class="author-name">Tobin Wells</p>
    </section>
  </main>
</body>
</html>
```